Business card to be used as a flyer

This business card should do the trick of a full scale flyer , so basicaly from the business card itself we only keep the size and remove the clasical name , position , company name (etc).
This business cards should be , like said above, used as promo tool, being gived to different girls . So base one : the design is girls oriented.
Colors : black background . We will use gold (color) folio for the text.
Attached you have our logo, but this should not be a proiminent part of the design . You can use only the cat head instead.
Target Market(s)
Girls / Women
Contact Information for Business Card
> black background , gold / folio text and elements
> cat head from the logo in a creative way do be displayed
> proieminent text "your path to success starts here"
> contact details phone and website .
www.velmastrand.ro (website) and 0742163958 (phone)

```html
<!DOCTYPE html>
<html lang="en">
<head>
<meta charset="utf-8">
<title>Velmastrand promo card</title>
<link href="https://fonts.googleapis.com/css2?family=Cormorant+Garamond:ital,wght@0,500;1,500&display=swap" rel="stylesheet">
<style>
  :root {
    --card-black: #0b0b0b;
    --gold: #d8b66a;
    --gold-deep: #a88a3c;
    --ink: #1a1a1a;
  }
  html, body {
    margin: 0;
    padding: 0;
    width: 1200px;
    height: 785px;
    overflow: hidden;
    background: var(--card-black);
  }
  .card {
    position: relative;
    width: 1200px;
    height: 785px;
    background: var(--card-black);
    overflow: hidden;
    font-family: "Cormorant Garamond", Georgia, serif;
    color: var(--gold);
  }
  .glitter-field {
    position: absolute;
    left: 0;
    right: 0;
    bottom: 0;
    height: 280px;
    background:
      radial-gradient(ellipse at 50% 100%, rgba(216,182,106,0.28) 0%, rgba(216,182,106,0.10) 45%, rgba(11,11,11,0) 75%),
      linear-gradient(to bottom, rgba(11,11,11,0) 0%, rgba(168,138,60,0.16) 100%);
  }
  .headline { position: absolute; margin: 0; font-weight: 500; line-height: 1; }
  .headline-lead {
    left: 570px; top: 212px;
    font-style: italic;
    font-size: 50px;
    transform: translateX(-50%);
    white-space: nowrap;
  }
  .headline-key {
    left: 80px; top: 268px;
    font-size: 128px;
    letter-spacing: 1px;
  }
  .headline-close {
    left: 392px; top: 410px;
    font-style: italic;
    font-size: 50px;
  }
  .contact-band {
    position: absolute;
    left: 0;
    top: 646px;
    width: 930px;
    height: 58px;
    background: var(--gold);
    display: flex;
    align-items: center;
    padding-left: 110px;
    box-sizing: border-box;
    gap: 26px;
  }
  .contact-item {
    display: flex;
    align-items: center;
    gap: 10px;
    font-size: 31px;
    color: var(--ink);
    white-space: nowrap;
  }
  .contact-icon { width: 26px; height: 26px; flex: none; }
  .brand-name {
    position: absolute;
    left: 960px;
    top: 370px;
    transform: translateX(-50%);
    font-size: 64px;
    font-weight: 500;
    color: var(--gold);
    white-space: nowrap;
  }
</style>
</head>
<body>
<main class="card">
  <div class="glitter-field" role="img" aria-label="Scattered gold glitter sparkles along the bottom of the card"></div>

  <p class="headline headline-lead">your path to</p>
  <p class="headline headline-key">Success</p>
  <p class="headline headline-close">starts here</p>

  <div class="brand-name">Velmastrand</div>

  <div class="contact-band">
    <span class="contact-item">
      <svg class="contact-icon" viewBox="0 0 26 26" aria-hidden="true">
        <circle cx="13" cy="13" r="13" fill="var(--ink)"/>
        <rect x="6.5" y="8.5" width="13" height="9" fill="none" stroke="var(--gold)" stroke-width="1.6"/>
        <path d="M6.5 8.5 L13 13.5 L19.5 8.5" fill="none" stroke="var(--gold)" stroke-width="1.6"/>
      </svg>
      www.velmastrand.ro
    </span>
    <span class="contact-item">
      <svg class="contact-icon" viewBox="0 0 26 26" aria-hidden="true">
        <circle cx="13" cy="13" r="13" fill="var(--ink)"/>
        <path d="M9 6.5 L11.5 9.5 L10 11.5 Q11.5 14.5 14.5 16 L16.5 14.5 L19.5 17 L18 19.5 Q11 19.5 6.5 11 Q6.5 8 9 6.5 Z" fill="var(--gold)"/>
      </svg>
      0742163958
    </span>
  </div>
</main>
</body>
</html>
```